Social Media Overlay for Ormond Real Estate

We need an social media overlay that can be added to a photo of a house that includes our current logo and a call to action of "Just Listed". This needs to be something that we can use for every new house that we list. Attached is our current logo in both company colors, purple and white. An example of a overlay from Plazeo that we like.

Target Market(s)

Social Media Real Estate Community - Real Estate Agents, Brokers, Buyers & Sellers

Industry/Entity Type

Real Estate

Font styles to use
Sans Serif

Colors
6c459b

Requirements
Must have
• the company colors, purple and white and the company logo
Nice to have
• call to action "Just Listed"
• some layered, texture, or 3-D effect
Should not have
• Should be clean and simple; nothing too busy

```html
<!DOCTYPE html>
<html lang="en">
<head>
<meta charset="utf-8">
<title>Ormond Real Estate – Just Listed</title>
<link rel="stylesheet" href="https://fonts.googleapis.com/css2?family=Open+Sans:wght@700&family=Aleo:wght@700&display=swap">
<style>
  :root {
    --brand-purple: #6c459b;
    --brand-white: #ffffff;
    --sky: #9fc3e4;
    --trees: #2f4a36;
    --house: #313c63;
    --lawn: #4f8a2e;
  }
  * { margin: 0; padding: 0; box-sizing: border-box; }
  html, body {
    width: 1200px;
    height: 1200px;
    overflow: hidden;
    background: var(--brand-white);
  }
  .overlay {
    position: relative;
    width: 1200px;
    height: 1200px;
    overflow: hidden;
  }
  .house-photo {
    position: absolute;
    inset: 0;
    background: linear-gradient(180deg,
      var(--sky) 0%,
      #c9dbea 12%,
      var(--trees) 24%,
      #3a4a5e 34%,
      var(--house) 48%,
      #3d3e4a 66%,
      #8a8577 72%,
      var(--lawn) 80%,
      #3f7a25 100%);
  }
  .top-band {
    position: absolute;
    left: 0;
    top: 0;
    width: 100%;
    height: 53px;
    background: var(--brand-purple);
  }
  .brand-panel {
    position: absolute;
    left: 29px;
    top: 1003px;
    width: 1142px;
    height: 197px;
    background: var(--brand-purple);
    border-radius: 38px 38px 0 0;
    box-shadow: 0 -4px 14px rgba(0,0,0,0.25);
  }
  .brand-name {
    position: absolute;
    left: 62px;
    top: 34px;
    color: var(--brand-white);
    font-family: "Open Sans", sans-serif;
    font-weight: 700;
    line-height: 1;
  }
  .brand-name .primary {
    display: block;
    font-size: 78px;
    letter-spacing: -2px;
  }
  .brand-name .secondary {
    display: block;
    font-size: 32px;
    margin-top: 8px;
    margin-left: 4px;
  }
  .cta-box {
    position: absolute;
    left: 462px;
    top: 34px;
    width: 656px;
    height: 140px;
    background: var(--brand-white);
    border-radius: 30px;
    display: flex;
    align-items: center;
    justify-content: center;
    box-shadow: inset 0 3px 8px rgba(0,0,0,0.18);
  }
  .cta-text {
    font-family: "Aleo", serif;
    font-weight: 700;
    font-size: 98px;
    color: var(--brand-purple);
    line-height: 1;
    letter-spacing: 1px;
  }
</style>
</head>
<body>
  <main class="overlay">
    <div class="house-photo" role="img" aria-label="Photo of a navy blue craftsman house with white trim, stone column bases, a wooden front door, tall evergreen trees behind and a green lawn in front"></div>
    <div class="top-band"></div>
    <section class="brand-panel">
      <div class="brand-name">
        <span class="primary">Ormond</span>
        <span class="secondary">Real Estate</span>
      </div>
      <div class="cta-box">
        <span class="cta-text">Just Listed</span>
      </div>
    </section>
  </main>
</body>
</html>
```